ZMobvra - Tenant Place Services

Want Quality Tenants?!

Tenant Placement is a service that allows landlords to leave the stress of filling vacancies behind.
zMobvra provides landlords, investors and property manager's a system to occupy vacancies with qualified tenants Faster, Cheaper, Easier
zMobvra takes the hassle out of the rental process from searching for tenants to move-in inspections.

Reason: I'm extending the deadline because I want to give other designers an opportunity to submit and I have a couple designs that I'm awaiting current designers to resubmit some designs.

```html
<!DOCTYPE html>
<html lang="en">
<head>
<meta charset="utf-8">
<title>zMobvra – Tenant Placement</title>
<link href="https://fonts.googleapis.com/css2?family=Arimo:wght@400;700&display=swap" rel="stylesheet">
<style>
  :root {
    --lime: #8dc63f;
    --white: #ffffff;
    --ink-grey: #6d6e70;
    --night-dark: #1b1b1b;
    --night-mid: #4a4a4a;
    --night-light: #8a8a8a;
  }
  * { margin: 0; padding: 0; box-sizing: border-box; }
  html, body {
    width: 1200px;
    height: 840px;
    overflow: hidden;
    background: var(--night-dark);
  }
  .ad {
    position: relative;
    width: 1200px;
    height: 840px;
    overflow: hidden;
    font-family: "Arimo", Arial, sans-serif;
    color: var(--white);
  }
  .city-backdrop {
    position: absolute;
    inset: 0;
    background:
      radial-gradient(ellipse at 62% 38%, rgba(200,200,200,0.35) 0%, rgba(0,0,0,0) 45%),
      linear-gradient(180deg, var(--night-light) 0%, var(--night-mid) 28%, #2c2c2c 60%, var(--night-dark) 100%);
  }
  .brand-badge {
    position: absolute;
    left: -125px;
    top: 127px;
    width: 466px;
    height: 466px;
    border-radius: 50%;
    background: var(--white);
    border: 14px solid var(--lime);
    z-index: 2;
  }
  .brand-name {
    position: absolute;
    left: 0;
    top: 432px;
    width: 216px;
    text-align: center;
    font-size: 46px;
    font-weight: 400;
    letter-spacing: 1px;
    color: var(--ink-grey);
    z-index: 3;
  }
  .headline-band {
    position: absolute;
    left: 300px;
    top: 295px;
    width: 900px;
    height: 137px;
    background: var(--lime);
    z-index: 1;
  }
  .headline {
    position: absolute;
    left: 341px;
    top: 295px;
    width: 859px;
    height: 137px;
    display: flex;
    align-items: center;
    justify-content: center;
    font-size: 62px;
    font-weight: 700;
    letter-spacing: 1px;
    z-index: 3;
  }
  .pitch {
    position: absolute;
    left: 420px;
    top: 480px;
    width: 740px;
    text-align: center;
    font-size: 45px;
    font-weight: 700;
    line-height: 72px;
    letter-spacing: 1px;
    text-shadow: 0 2px 6px rgba(0,0,0,0.6);
  }
  .web-address {
    position: absolute;
    right: 24px;
    bottom: 22px;
    font-size: 32px;
    font-weight: 700;
    letter-spacing: 0.5px;
    text-shadow: 0 2px 6px rgba(0,0,0,0.6);
  }
</style>
</head>
<body>
  <div class="ad">
    <div class="city-backdrop" role="img" aria-label="Black and white night skyline of tall city buildings with lit windows"></div>
    <div class="headline-band"></div>
    <div class="brand-badge"></div>
    <div class="brand-name">zMobvra</div>
    <div class="headline">NEED TENANTS?!</div>
    <p class="pitch">FILL YOUR VACANCY<br>FASTER, EASIER, CHEAPER</p>
    <p class="web-address">@ ZMOBVRA.COM</p>
  </div>
</body>
</html>
```